Need a new letterhead

Need a new fresh exciting letterhead. Remove the footer...info is outdated.

Target Market(s)

B2B

Industry/Entity Type

Electrical Power

Colors

Designer to choose colors to be used in the design.

Requirements
Must have
• Red and Blue Corvane Systems Logo
Nice to have
• Lighting the way to sustainability in footer...reorganize the words?

```html
<!DOCTYPE html>
<html lang="en">
<head>
<meta charset="UTF-8">
<title>Corvane Systems Letterhead</title>
<link href="https://fonts.googleapis.com/css2?family=Lato:ital,wght@0,300;0,400;0,700;1,900&display=swap" rel="stylesheet">
<style>
  :root {
    --backdrop: #bdbdbd;
    --paper: #ffffff;
    --ink: #2b2b2b;
    --muted: #6a6a6a;
    --brand-red: #e8202a;
    --brand-blue: #2b3a86;
    --name-red: #a3151c;
  }
  * { margin: 0; padding: 0; box-sizing: border-box; }
  html, body { width: 1082px; height: 1200px; overflow: hidden; }
  body { background: var(--backdrop); font-family: "Lato", sans-serif; color: var(--ink); position: relative; }
  .letterhead { position: absolute; left: 166px; top: 119px; width: 750px; height: 982px; background: var(--paper); }
  .brand { position: absolute; top: 44px; left: 0; width: 100%; text-align: center; font-weight: 700; font-size: 30px; color: var(--brand-red); letter-spacing: 0.5px; }
  .recipient { position: absolute; left: 67px; top: 152px; }
  .recipient .label { font-size: 15px; font-weight: 400; color: #111; margin-bottom: 16px; }
  .recipient .name { font-size: 15px; color: var(--name-red); line-height: 1; }
  .recipient .role { font-size: 10px; color: var(--muted); line-height: 1.2; }
  .recipient .line { font-size: 15px; line-height: 17px; }
  .body-copy { position: absolute; left: 67px; top: 286px; width: 640px; font-size: 14.5px; font-weight: 300; line-height: 17.2px; }
  .body-copy p { margin-bottom: 17.2px; }
  .body-copy p.spaced { margin-top: 17px; }
  .signoff { position: absolute; left: 67px; top: 803px; font-size: 14px; font-weight: 900; font-style: italic; color: #111; }
  .signature { position: absolute; left: 67px; top: 830px; width: 90px; height: 26px; background: linear-gradient(90deg, #3a3a3a22, #3a3a3a44); border-radius: 4px; }
  .footer { position: absolute; left: 0; bottom: 0; width: 750px; height: 42px; }
</style>
</head>
<body>
  <div class="letterhead">
    <div class="brand">Corvane Systems</div>

    <div class="recipient">
      <div class="label">TO</div>
      <div class="name">HARLOW</div>
      <div class="role">Director</div>
      <div class="line">Design Studio</div>
      <div class="line">A: 140 372 618</div>
      <div class="line">B:8124&nbsp; 309 776</div>
    </div>

    <div class="body-copy">
      <p>Lorem ipsum dolor sit amet, consectetur adipiscing elit. Vestibulum consectetur egestas metus, quis scelerisque tortor consectetur sed. Nullam sit amet lorem sed arcu faucibus semper. Vestibulum ante ipsum primis in faucibus orci luctus et ultrices posuere cubilia Curae; Sed sagittis arcu ut ligula molestie malesuada. Suspendisse posuere tincidunt elit, at ullamcorper augue blandit vitae.</p>
      <p>Cras egestas vestibulum pulvinar. Donec iaculis imperdiet hendrerit. Sed mollis, enim quis hendrerit dictum, tortor mauris vulputate ligula, viverra porta magna libero at mi. Integer odio nisl, luctus nec dui in, rutrum sollicitudin nisi. Suspendisse nec erat eros.</p>
      <p>Sed dictum quam arcu, sit amet ullamcorper orci faucibus eget. Morbi finibus ante at risus commodo, nec ullamcorper nulla tincidunt. Integer eu molestie nulla, sed consequat tortor. Sed ullamcorper congue metus, vitae dictum nibh luctus sed. Suspendisse ornare purus fermentum, viverra elit sed, bibendum ex. Vivamus semper diam vel diam laoreet rutrum. Ut porta fermentum velit. Vestibulum vitae semper nisl. Sed facilisis at ex et vestibulum. Donec at magna ut eros pulvinar hendrerit.</p>
      <p class="spaced">Sed dictum quam arcu, sit amet ullamcorper orci faucibus eget. Morbi finibus ante at risus commodo, nec ullamcorper nulla tincidunt. Integer eu molestie nulla, sed consequat tortor. Sed ullamcorper congue metus, vitae dictum nibh luctus sed. Suspendisse ornare purus fermentum, viverra elit sed, bibendum ex.</p>
      <p>Vivamus semper diam vel diam laoreet rutrum. Ut porta fermentum velit. Vestibulum vitae semper nisl. Sed facilisis at ex et vestibulum. Donec at magna ut eros pulvinar hendrerit.</p>
    </div>

    <div class="signoff">Regards,</div>
    <div class="signature" role="img" aria-label="Handwritten signature"></div>

    <svg class="footer" viewBox="0 0 750 42" xmlns="http://www.w3.org/2000/svg">
      <rect x="0" y="34" width="750" height="8" fill="var(--brand-red)"/>
      <line x1="84" y1="32" x2="676" y2="32" stroke="var(--brand-blue)" stroke-width="2"/>
      <polygon points="264,32 284,3 292,3 272,32" fill="var(--brand-blue)"/>
      <polygon points="486,32 466,3 474,3 494,32" fill="var(--brand-blue)"/>
      <polygon points="274,32 294,3 465,3 484,32" fill="var(--brand-red)"/>
      <g fill="#ffffff" font-family="Lato, sans-serif" font-size="5">
        <circle cx="297" cy="18" r="2.3" fill="none" stroke="#fff" stroke-width="0.7"/>
        <text x="302" y="20">0097315550182</text>
        <rect x="348" y="16" width="5" height="3.5" fill="none" stroke="#fff" stroke-width="0.6"/>
        <text x="355" y="20">info@corvane-sys.com</text>
        <rect x="406" y="16" width="5" height="4" />
        <text x="414" y="20">0097315550197</text>
      </g>
    </svg>
  </div>
</body>
</html>
```